BRISKWATER MOTION GYM FLYER DESIGN

We want a flyer designed for our gym. We have an example of a flyer which we like and I have put it into the images I have uploaded. I would like to recreate using our pictures, so its a pretty straight forward job. We also want to put our weekly timetable on the back of the flyer. We would like the size of the flyer to be A5.

Target Market(s)

FITNESS

Industry/Entity Type

Gym

Colors
33a6d7
ffffff

Requirements
Must have
• We just want to recreate the flyer but we must have the following info on the flyer and we want our timetable on the back of the flyer which you can get from this link: http://www.briskwatermotiongym.com/timetable
• Briskwater Motion Gym is a fun community of humble people. Our goal is to help guide you towards a fitter, healthier lifestyle!
• Our Programs
• HIIT
• High intensity interval training is 30-45 minutes of fat burning fun. The class is a mix of cardio, bodyweight and some resistance movements.
• Conditioning
• A full hour of strength, cardio and bodyweight training to get you in tip top shape. Expect a mix of barbells, kettlebells, rowing machines, bikes and other training methods.
• KPL
• This is our big Friday session to set you up for the weekend. 90 minutes of hard training that is done with a team emphasis. From heavy lifting to cardio triathlons, this class has it all but not for the faint hearted.
• Muay Thai
• Commonly known as the science of 8 limbs you will learn how to punch, kick, knee and elbow. Thailands national sport is a great way to get your fitness kick. We train the complete beginner all the way to international fighters so you are in great hands.
• Kids Muay Thai
• Our junior program starts from age 6 onwards. Muay Thai is a great way for kids to get active and fit while learning new skills. Training in martial arts also teaches self discipline and socialisation skills.
• Yoga
• A combination of physical and mental practises that will leave you focused and refreshed for whatever the week throws at you. We always recommend our yoga classes as a great way to balance the high intensity training we offer.
• U-Press
• Strength training with a little bit of conditioning. We regularly update the program and re test lifts to ensure you are making progress and getting stronger.
• CONTACT US
• OUR LOCATION:
• Unit 42C
• 273 Quillan Street
• Fenwick Hollow
• Glasgow
• G72TR
• Phone: 07950362814
• Email: info@briskwatermotiongym.com
• Web: www.briskwatermotiongym.com
Nice to have
• Can use all the picture but if not be good to use the boxing one and the group training one.

```html
<!DOCTYPE html>
<html lang="en">
<head>
<meta charset="utf-8">
<title>Briskwater Motion Gym – Flyer</title>
<link href="https://fonts.googleapis.com/css2?family=Barlow+Condensed:wght@400;500;600&family=Open+Sans:ital,wght@0,400;0,600;1,600&display=swap" rel="stylesheet">
<style>
:root{
  --sky:#33a6d7;
  --white:#ffffff;
  --stage:#1d4f57;
  --row-alt:#d9e9f5;
  --grid-line:#9cc9e4;
  --ink-blue:#2a8fc4;
  --olive:#667a45;
  --violet:#7a4c9f;
  --orchid:#c982c4;
  --teal:#2f6e86;
  --rust:#b3643a;
  --crimson:#c0392f;
  --tangerine:#e27b2d;
  --navy:#1d3c4c;
  --ice:#d5ecf8;
  --lime:#3fae4a;
  --cocoa:#6b3d25;
  --azure:#3b7fc2;
  --head:'Barlow Condensed', sans-serif;
  --body:'Open Sans', sans-serif;
}
*{box-sizing:border-box;margin:0;padding:0}
html,body{width:1200px;height:928px;overflow:hidden}
body{background:var(--stage);position:relative;font-family:var(--body)}
.page{position:absolute;top:68px;width:560px;height:792px;overflow:hidden}
.front{left:30px;background:var(--white)}
.back{left:610px;background:var(--sky)}

/* front */
.hero-photo{position:absolute;left:0;top:0;width:560px;height:310px;
  background:linear-gradient(120deg,#cfc9c4 0%,#9b8f88 35%,#b45a4a 60%,#6f6561 80%,#3f3a38 100%)}
.program-band{position:absolute;left:0;top:244px;width:560px;height:438px;background:var(--sky);
  clip-path:polygon(0 57px,100% 0,100% 100%,0 100%)}
.quote-card{position:absolute;left:74px;top:258px;width:336px;height:80px;background:var(--white);
  transform:rotate(-3deg);box-shadow:0 2px 4px rgba(0,0,0,.15);padding:12px 12px 0 44px;
  color:var(--ink-blue);font-weight:600;font-size:12px;line-height:18px}
.quote-card .mark{position:absolute;left:14px;top:4px;font-family:var(--head);font-size:44px;line-height:44px;font-weight:600;color:var(--ink-blue)}
.section-title{position:absolute;left:21px;top:352px;font-family:var(--head);font-weight:500;font-size:32px;line-height:36px;color:var(--white);letter-spacing:.5px}
.program{position:absolute;color:var(--white)}
.program h3{font-family:var(--head);font-weight:400;font-size:14px;line-height:15px;display:flex;align-items:center;gap:7px}
.program h3 svg{flex:none}
.program p{font-size:8.3px;line-height:11px;text-align:justify;margin-left:20px;margin-top:1px}
.col-l{left:21px;width:258px}
.col-r{left:284px;width:256px}
.training-photo{position:absolute;left:400px;top:527px;width:160px;height:170px;
  background:linear-gradient(160deg,#5a5a5a,#2e2e2e 60%,#1a1a1a)}
.front-footer{position:absolute;left:0;top:682px;width:560px;height:110px;color:var(--ink-blue)}
.brand{position:absolute;width:112px;display:flex;flex-direction:column;align-items:center;gap:6px;font-family:var(--head);font-weight:600;font-size:12px;letter-spacing:.5px;white-space:nowrap}
.brand .dot{width:22px;height:22px;border-radius:50%;background:currentColor}
.front-footer .brand{left:22px;top:34px}
.contact{position:absolute;font-family:var(--head);font-size:12.5px;line-height:15.5px;font-weight:400;white-space:nowrap}
.contact b{font-weight:600}
.front-footer .loc{left:156px;top:24px}
.front-footer .net{left:342px;top:24px}
.social{display:flex;gap:4px;margin-top:5px}
.social span{width:13px;height:13px;background:var(--ink-blue);border-radius:2px}

/* back */
.header-photo{position:absolute;left:0;top:0;width:230px;height:150px;
  background:radial-gradient(ellipse at 35% 35%,rgba(255,255,255,.28),rgba(255,255,255,0) 70%)}
.tt-title{position:absolute;left:0;width:560px;top:22px;text-align:center;font-family:var(--head);font-weight:600;font-size:44px;color:var(--white);letter-spacing:.5px}
.tt-sub{position:absolute;left:0;width:560px;top:71px;text-align:center;font-size:9.4px;color:var(--white)}
.timetable{position:absolute;left:37px;top:90px;width:485px;height:598px;display:grid;
  grid-template-columns:43px repeat(7,1fr);grid-template-rows:15px repeat(38,1fr);
  background-color:var(--white);
  background-image:repeating-linear-gradient(to bottom,var(--white) 0 15.34px,var(--row-alt) 15.34px 30.68px);
  background-position:0 15px;background-repeat:repeat-x}
.timetable .head{grid-row:1;background:var(--white);border-bottom:1px solid var(--grid-line);font-family:var(--head);font-size:10px;color:#2a6f94;text-align:center;line-height:15px}
.col-line{grid-row:1/40;border-right:1px solid var(--grid-line)}
.hour{grid-column:1;font-family:var(--head);font-size:10px;color:#2a4f66;padding:2px 0 0 10px;border-top:1px solid var(--grid-line)}
.slot{margin:1px;color:var(--white);font-family:var(--head);font-size:9.5px;line-height:9.5px;display:flex;align-items:center;justify-content:center;text-align:center;border-radius:1px;box-shadow:0 1px 1px rgba(0,0,0,.25);overflow:hidden;min-width:0}
.slot.tiny{font-size:6px;line-height:6.5px}
.slot.thin{margin:3px 1px}
.split{margin:1px;display:flex;gap:1px;min-width:0}
.split .slot{margin:0;flex:1}
.olive{background:var(--olive)}.violet{background:var(--violet)}.orchid{background:var(--orchid)}
.teal{background:var(--teal)}.rust{background:var(--rust)}.crimson{background:var(--crimson)}
.tangerine{background:var(--tangerine)}.navy{background:var(--navy)}.lime{background:var(--lime)}
.ice{background:var(--ice);color:#6aa6c8}.cocoa{background:var(--cocoa)}.azure{background:var(--azure)}
.vert{writing-mode:vertical-rl;transform:rotate(180deg)}
.back-footer{position:absolute;left:0;top:700px;width:560px;height:92px;color:var(--white)}
.back-footer .brand{left:36px;top:24px}
.back-footer .loc{left:162px;top:12px}
.back-footer .net{left:339px;top:12px;line-height:18px}
</style>
</head>
<body>

<section class="page front">
  <div class="hero-photo" role="img" aria-label="Photo of a boxer striking pads held by a trainer in a boxing ring"></div>
  <div class="program-band"></div>
  <div class="quote-card"><span class="mark">“</span>Briskwater Motion Gym is a fun community of humble people. Our goal is to help guide you towards a fitter, healthier lifestyle!</div>

  <h2 class="section-title">OUR PROGRAMS</h2>

  <div class="program col-l" style="top:392px">
    <h3><svg width="12" height="12" viewBox="0 0 12 12"><circle cx="6" cy="6" r="5.5" fill="#fff"/><circle cx="6" cy="6" r="2.4" fill="#33a6d7"/></svg>HIIT</h3>
    <p>High intensity interval training is 30-45 minutes of fat burning fun. The class is a mix of cardio, bodyweight and some resistance movements.</p>
  </div>
  <div class="program col-l" style="top:450px">
    <h3><svg width="12" height="12" viewBox="0 0 12 12"><circle cx="6" cy="6" r="5.5" fill="#fff"/><circle cx="6" cy="6" r="2.4" fill="#33a6d7"/></svg>CONDITIONING</h3>
    <p>A full hour of strength, cardio and bodyweight training to get you in tip top shape. Expect a mix of barbells, kettlebells, rowing machines, bikes and other training methods.</p>
  </div>
  <div class="program col-l" style="top:517px">
    <h3><svg width="12" height="12" viewBox="0 0 12 12"><circle cx="6" cy="6" r="5.5" fill="#fff"/><circle cx="6" cy="6" r="2.4" fill="#33a6d7"/></svg>KPL</h3>
    <p>This is our big Friday session to set you up for the weekend. 90 minutes of hard training that is done with a team emphasis. From heavy lifting to cardio triathlons, this class has it all but not for the faint hearted.</p>
  </div>
  <div class="program col-l" style="top:596px">
    <h3><svg width="12" height="12" viewBox="0 0 12 12"><circle cx="6" cy="6" r="5.5" fill="#fff"/><circle cx="6" cy="6" r="2.4" fill="#33a6d7"/></svg>MUAY THAI</h3>
    <p>Commonly known as the science of 8 limbs you will learn how to punch, kick, knee and elbow. Thailands national sport is a great way to get your fitness kick. We train the complete beginner all the way to international fighters so you are in great hands.</p>
  </div>

  <div class="program col-r" style="top:392px">
    <h3><svg width="12" height="12" viewBox="0 0 12 12"><circle cx="6" cy="6" r="5.5" fill="#fff"/><circle cx="6" cy="6" r="2.4" fill="#33a6d7"/></svg>KIDS MUAY THAI</h3>
    <p>Our junior program starts from age 6 onwards. Muay Thai is a great way for kids to get active and fit while learning new skills. Training in martial arts also teaches self discipline and socialisation skills.</p>
  </div>
  <div class="program col-r" style="top:461px">
    <h3><svg width="12" height="12" viewBox="0 0 12 12"><circle cx="6" cy="6" r="5.5" fill="#fff"/><circle cx="6" cy="6" r="2.4" fill="#33a6d7"/></svg>YOGA</h3>
    <p>A combination of physical and mental practises that will leave you focused and refreshed for whatever the week throws at you. We always recommend our yoga classes as a great way to balance the high intensity training we offer.</p>
  </div>
  <div class="program col-r" style="top:540px;width:112px">
    <h3><svg width="12" height="12" viewBox="0 0 12 12"><circle cx="6" cy="6" r="5.5" fill="#fff"/><circle cx="6" cy="6" r="2.4" fill="#33a6d7"/></svg>U-PRESS</h3>
    <p>Strength training with a little bit of conditioning. We regularly update the program and re test lifts to ensure you are making progress and getting stronger.</p>
  </div>
  <div class="training-photo" role="img" aria-label="Black and white photo of a man training with a kettlebell in the gym"></div>

  <footer class="front-footer">
    <div class="brand"><span class="dot"></span>BRISKWATER MOTION</div>
    <div class="contact loc"><b>OUR LOCATION:</b><br>Unit 42C, 273 Quillan Street,<br>Fenwick Hollow, Glasgow G72TR<br><b>Phone:</b> 07950362814</div>
    <div class="contact net"><b>Email:</b> info@briskwatermotiongym.com<br><b>Web:</b> www.briskwatermotiongym.com
      <div class="social"><span></span><span></span><span></span><span></span></div>
    </div>
  </footer>
</section>

<section class="page back">
  <div class="header-photo" role="img" aria-label="Faint photo of an athlete training"></div>
  <h1 class="tt-title">TIMETABLE</h1>
  <p class="tt-sub">See below for our full timetable of classes please see our Website for more info and class descriptions</p>

  <div class="timetable">
    <div class="head" style="grid-column:1"></div>
    <div class="head" style="grid-column:2">SUN</div>
    <div class="head" style="grid-column:3">MON</div>
    <div class="head" style="grid-column:4">TUE</div>
    <div class="head" style="grid-column:5">WED</div>
    <div class="head" style="grid-column:6">THU</div>
    <div class="head" style="grid-column:7">FRI</div>
    <div class="head" style="grid-column:8">SAT</div>
    <div class="col-line" style="grid-column:1"></div><div class="col-line" style="grid-column:2"></div>
    <div class="col-line" style="grid-column:3"></div><div class="col-line" style="grid-column:4"></div>
    <div class="col-line" style="grid-column:5"></div><div class="col-line" style="grid-column:6"></div>
    <div class="col-line" style="grid-column:7"></div>

    <div class="hour" style="grid-row:2">5 AM</div><div class="hour" style="grid-row:4">6 AM</div>
    <div class="hour" style="grid-row:6">7 AM</div><div class="hour" style="grid-row:8">8 AM</div>
    <div class="hour" style="grid-row:10">9 AM</div><div class="hour" style="grid-row:12">10 AM</div>
    <div class="hour" style="grid-row:14">11 AM</div><div class="hour" style="grid-row:16">12 PM</div>
    <div class="hour" style="grid-row:18">1 PM</div><div class="hour" style="grid-row:20">2 PM</div>
    <div class="hour" style="grid-row:22">3 PM</div><div class="hour" style="grid-row:24">4 PM</div>
    <div class="hour" style="grid-row:26">5 PM</div><div class="hour" style="grid-row:28">6 PM</div>
    <div class="hour" style="grid-row:30">7 PM</div><div class="hour" style="grid-row:32">8 PM</div>
    <div class="hour" style="grid-row:34">9 PM</div><div class="hour" style="grid-row:36">10 PM</div>
    <div class="hour" style="grid-row:38">11 PM</div>

    <!-- Monday -->
    <div class="slot olive" style="grid-column:3;grid-row:6/8">Conditioning</div>
    <div class="slot violet" style="grid-column:3;grid-row:8/12">Open Gym</div>
    <div class="slot orchid" style="grid-column:3;grid-row:12/14">U-Press</div>
    <div class="slot tangerine tiny thin" style="grid-column:3;grid-row:16/17">LUNCH TIME HIIT</div>
    <div class="slot violet" style="grid-column:3;grid-row:24/26">Open Gym</div>
    <div class="slot orchid" style="grid-column:3;grid-row:26/28;margin-right:50%">U-Press</div>
    <div class="split" style="grid-column:3;grid-row:28/30"><div class="slot orchid" style="flex:.3"></div><div class="slot azure tiny" style="flex:.4"><span class="vert">Kids</span></div><div class="slot teal tiny" style="flex:1.3">Muay Thai Foundation</div></div>
    <div class="slot rust" style="grid-column:3;grid-row:30/32">Strength &amp; Conditioning</div>

    <!-- Tuesday -->
    <div class="slot orchid" style="grid-column:4;grid-row:4/6">U-Press</div>
    <div class="slot teal" style="grid-column:4;grid-row:6/8">Fight Camp Muay Thai</div>
    <div class="slot violet" style="grid-column:4;grid-row:8/12">Open Gym</div>
    <div class="slot tangerine tiny thin" style="grid-column:4;grid-row:16/17">LUNCH TIME HIIT</div>
    <div class="slot violet" style="grid-column:4;grid-row:24/28;margin-right:50%">Open Gym</div>
    <div class="slot tangerine tiny" style="grid-column:4;grid-row:27/28;margin-left:50%">HIIT (13/30)</div>
    <div class="split" style="grid-column:4;grid-row:28/30"><div class="slot olive tiny">Conditioning</div><div class="slot ice tiny">Kids</div></div>
    <div class="slot navy" style="grid-column:4;grid-row:30/32">Muay Thai Intermediate</div>

    <!-- Wednesday -->
    <div class="slot rust" style="grid-column:5;grid-row:4/6">Strength &amp; Conditioning</div>
    <div class="slot crimson" style="grid-column:5;grid-row:6/8">Yoga [5/25]</div>
    <div class="slot violet" style="grid-column:5;grid-row:8/12">Open Gym</div>
    <div class="slot orchid" style="grid-column:5;grid-row:12/14">U-Press</div>
    <div class="slot violet" style="grid-column:5;grid-row:24/26">Open Gym</div>
    <div class="slot orchid" style="grid-column:5;grid-row:26/28;margin-right:50%">U-Press</div>
    <div class="slot tangerine tiny" style="grid-column:5;grid-row:27/28;margin-left:50%">HIIT (13/30)</div>
    <div class="split" style="grid-column:5;grid-row:28/30"><div class="slot orchid" style="flex:.3"></div><div class="slot azure tiny" style="flex:.4"><span class="vert">Kids</span></div><div class="slot teal tiny" style="flex:1.3">Muay Thai Foundation</div></div>
    <div class="slot crimson" style="grid-column:5;grid-row:30/33">Yoga [5/25]</div>

    <!-- Thursday -->
    <div class="slot olive" style="grid-column:6;grid-row:6/8">Conditioning</div>
    <div class="slot violet" style="grid-column:6;grid-row:8/12">Open Gym</div>
    <div class="slot tangerine tiny thin" style="grid-column:6;grid-row:16/17">LUNCH TIME HIIT</div>
    <div class="slot violet" style="grid-column:6;grid-row:24/28;margin-right:50%">Open Gym</div>
    <div class="slot tangerine tiny" style="grid-column:6;grid-row:27/28;margin-left:50%">HIIT (13/30)</div>
    <div class="split" style="grid-column:6;grid-row:28/30"><div class="slot olive tiny">Conditioning</div><div class="slot ice tiny">Kids</div></div>
    <div class="slot navy" style="grid-column:6;grid-row:30/32">Muay Thai Intermediate</div>

    <!-- Friday -->
    <div class="slot orchid" style="grid-column:7;grid-row:4/6">U-Press</div>
    <div class="slot teal" style="grid-column:7;grid-row:6/8">Fight Camp Muay Thai</div>
    <div class="slot violet" style="grid-column:7;grid-row:8/12">Open Gym</div>
    <div class="slot orchid" style="grid-column:7;grid-row:12/14">U-Press</div>
    <div class="slot tangerine tiny thin" style="grid-column:7;grid-row:16/17">LUNCH TIME HIIT</div>
    <div class="slot violet" style="grid-column:7;grid-row:24/26">Open Gym</div>
    <div class="slot orchid" style="grid-column:7;grid-row:26/28;margin-right:50%">U-Press</div>
    <div class="slot lime tiny" style="grid-column:7;grid-row:28/31;margin-left:50%;align-items:flex-start;padding-top:2px">KPL</div>

    <!-- Saturday -->
    <div class="slot cocoa" style="grid-column:8;grid-row:12/14">Saturday Circuit</div>
    <div class="split" style="grid-column:8;grid-row:14/18">
      <div class="slot violet tiny" style="flex:.5"><span class="vert">Open Gym</span></div>
      <div style="flex:1.5;display:flex;flex-direction:column;gap:1px;min-width:0">
        <div style="flex:1;display:flex;gap:1px"><div class="slot azure tiny" style="flex:.4"><span class="vert">Kids</span></div><div class="slot ice tiny">Kids</div></div>
        <div style="flex:1;display:flex;gap:1px"><div class="slot azure" style="flex:.4"></div><div class="slot teal tiny">Muay Thai Foundation</div></div>
      </div>
    </div>
  </div>

  <footer class="back-footer">
    <div class="brand"><span class="dot"></span>BRISKWATER MOTION</div>
    <div class="contact loc"><b>OUR LOCATION:</b><br>Unit 42C<br>273 Quillan Street, Fenwick Hollow<br>Glasgow G72TR</div>
    <div class="contact net"><b>Phone:</b> 07950362814<br><b>Email:</b> info@briskwatermotiongym.com<br><b>Web:</b> www.briskwatermotiongym.com</div>
  </footer>
</section>

</body>
</html>
```